Realty Group Needs Classy, Contemporary Letterhead Design

We need a letterhead design for a new realty company located in NY, USA. We buy investment properties to rehabilitate and or keep in our rental portfolio.

```html
<!DOCTYPE html>
<html lang="en">
<head>
<meta charset="utf-8">
<title>Meridian Crest Realty Group – Letterhead</title>
<link rel="stylesheet" href="https://fonts.googleapis.com/css2?family=Open+Sans:wght@400;600;700;800&display=swap">
<style>
  :root {
    --backdrop: #e8e8e8;
    --paper: #ffffff;
    --brand-purple: #3d1a78;
    --rule-grey: #6d6d6d;
    --text-grey: #5a5a5a;
    --text-dark: #3a3a3a;
  }
  * { box-sizing: border-box; margin: 0; padding: 0; }
  html, body {
    width: 1200px;
    height: 795px;
    overflow: hidden;
  }
  body {
    background: var(--backdrop);
    font-family: "Open Sans", Arial, sans-serif;
    position: relative;
  }
  .letterhead {
    position: absolute;
    left: 333px;
    top: 20px;
    width: 534px;
    height: 755px;
    background: var(--paper);
    box-shadow: 0 2px 10px rgba(0,0,0,0.12);
  }
  .letterhead-header {
    position: absolute;
    left: 34px;
    right: 34px;
    top: 34px;
    display: flex;
    justify-content: space-between;
    align-items: flex-end;
  }
  .brand {
    display: flex;
    flex-direction: column;
    align-items: flex-end;
    line-height: 1;
  }
  .brand-name-row {
    display: flex;
    align-items: center;
    gap: 5px;
  }
  .brand-dot {
    width: 9px;
    height: 9px;
    border-radius: 50%;
    background: var(--brand-purple);
  }
  .brand-name {
    font-weight: 800;
    font-size: 24px;
    letter-spacing: 0.3px;
    color: var(--brand-purple);
    text-transform: uppercase;
  }
  .brand-tagline {
    font-weight: 600;
    font-size: 7.5px;
    color: var(--text-grey);
    letter-spacing: 0.6px;
    margin-top: 3px;
  }
  .contact-list {
    list-style: none;
    text-align: right;
    font-size: 6px;
    line-height: 9px;
    color: var(--text-grey);
  }
  .contact-list li {
    display: flex;
    justify-content: flex-end;
    align-items: center;
    gap: 4px;
  }
  .contact-icon {
    width: 7px;
    height: 7px;
    flex: none;
  }
  .header-rule {
    position: absolute;
    left: 34px;
    right: 34px;
    top: 82px;
    height: 1.5px;
    background: linear-gradient(to right, var(--rule-grey) 0 68%, var(--brand-purple) 68% 100%);
  }
  .footer-rule-grey {
    position: absolute;
    left: 34px;
    right: 34px;
    bottom: 70px;
    height: 1.5px;
    background: var(--rule-grey);
  }
  .footer-rule-purple {
    position: absolute;
    left: 34px;
    right: 34px;
    bottom: 44px;
    height: 2px;
    background: var(--brand-purple);
  }
  .footer-address {
    position: absolute;
    left: 34px;
    bottom: 26px;
    font-size: 9.5px;
    color: var(--text-grey);
  }
  .footer-address strong {
    font-weight: 700;
    color: var(--text-dark);
  }
</style>
</head>
<body>
  <main class="letterhead">
    <header class="letterhead-header">
      <div class="brand">
        <div class="brand-name-row">
          <span class="brand-dot"></span>
          <span class="brand-name">Meridian</span>
        </div>
        <span class="brand-tagline">Realty Group, LLC</span>
      </div>
      <ul class="contact-list">
        <li>(000) 0123 456 789
          <svg class="contact-icon" viewBox="0 0 10 10"><circle cx="5" cy="5" r="5" fill="#3d1a78"/><path d="M3.3 2.6l1 1-.5.7a3 3 0 0 0 1.9 1.9l.7-.5 1 1-.6.8C4.8 7.3 2.7 5.2 2.6 3.2z" fill="#fff"/></svg>
        </li>
        <li>(000) 0123 456 790
          <svg class="contact-icon" viewBox="0 0 10 10"><circle cx="5" cy="5" r="5" fill="#3d1a78"/><path d="M3.3 2.6l1 1-.5.7a3 3 0 0 0 1.9 1.9l.7-.5 1 1-.6.8C4.8 7.3 2.7 5.2 2.6 3.2z" fill="#fff"/></svg>
        </li>
        <li>info@meridiancrestrealty.com
          <svg class="contact-icon" viewBox="0 0 10 10"><circle cx="5" cy="5" r="5" fill="#3d1a78"/><rect x="2.5" y="3.3" width="5" height="3.4" fill="none" stroke="#fff" stroke-width=".7"/><path d="M2.5 3.3L5 5.3l2.5-2" fill="none" stroke="#fff" stroke-width=".7"/></svg>
        </li>
        <li>www.meridiancrestrealty.com
          <svg class="contact-icon" viewBox="0 0 10 10"><circle cx="5" cy="5" r="5" fill="#3d1a78"/><circle cx="5" cy="5" r="2.6" fill="none" stroke="#fff" stroke-width=".7"/><path d="M2.4 5h5.2M5 2.4c-1.4 1.6-1.4 3.6 0 5.2M5 2.4c1.4 1.6 1.4 3.6 0 5.2" fill="none" stroke="#fff" stroke-width=".6"/></svg>
        </li>
      </ul>
    </header>
    <div class="header-rule"></div>

    <div class="footer-rule-grey"></div>
    <div class="footer-rule-purple"></div>
    <footer class="footer-address">
      <strong>Meridian Crest Realty Group, LLC</strong> : Suite 102 Street name, State, Zip 2034, Country
    </footer>
  </main>
</body>
</html>
```